Brightvale Crew Word Press Website

We need a graphical, fun website that conveys our messaging of providing the Best-In-Class Signature Marketing System for Mortgage Loan Officers and Realtors. Our system uses AI and Predictive Analysis to uncover the 'Gold' hidden in contact databases. The 'Gold' is defined as people who are in the market or likely to be in the market soon. We place that 'Gold' in the form of Contact Name, Address, Phone and Email on a Daily To Do List detailing what type of contact should be made.

Target Market(s)

Mortgage Loan Officers and Realtors

Industry/Entity Type

Mortgage & Real Estate

Coding

Coded - Design and coding required

Number of Pages Required

5+ page

Requirements
Must have
• I like the look of this site- https://www.homeloanpromostudio.example/
Nice to have
• Please create a flow that is similar to https://www.homeloanpromostudio.example/, but better, more dynamic. Site must be responsive and mobile friendly. Site will have embedded videos. Site need to convey a message of hope, imagination, innovation, results oriented, better than the rest, victory!
Should not have
• Nothing cheesy or low class.

```html
<!DOCTYPE html>
<html lang="en">
<head>
<meta charset="utf-8">
<title>Brightvale Crew — Full Service Mortgage Marketing</title>
<link href="https://fonts.googleapis.com/css2?family=Montserrat:wght@400;500;600;700&display=swap" rel="stylesheet">
<style>
:root{
  --blue:#1479f2;
  --blue-deep:#0a63d8;
  --blue-light:#5aa8ff;
  --gold:#f4c53a;
  --gold-deep:#dca31c;
  --ink:#222222;
  --grey-bg:#eeeeee;
  --dark:#1c1915;
  --dark-warm:#3a2f1d;
  --white:#ffffff;
  --text-soft:#444444;
}
*{margin:0;padding:0;box-sizing:border-box}
html,body{width:1200px;height:5181px;overflow:hidden}
body{font-family:'Montserrat',sans-serif;color:var(--ink);position:relative;background:var(--white)}
.abs{position:absolute}
.btn{position:absolute;display:flex;align-items:center;justify-content:center;border-radius:24px;
  background:linear-gradient(180deg,var(--gold),var(--gold-deep));color:var(--white);
  font-weight:600;font-size:15px;letter-spacing:1px;text-transform:uppercase}
.brand{position:absolute;display:flex;align-items:center;gap:10px;color:var(--gold);
  font-weight:700;font-size:22px;letter-spacing:1px;text-transform:uppercase;line-height:1.05}
.brand .dot{width:30px;height:30px;border-radius:50%;background:var(--gold);flex:none}

/* hero */
.hero{position:absolute;left:0;top:0;width:1200px;height:1011px;
  background:linear-gradient(110deg,#2b2620 0%,#3c3426 45%,#2f281d 100%)}
.topbar{position:absolute;left:430px;top:0;width:770px;height:54px;background:var(--blue);
  clip-path:polygon(40px 0,100% 0,100% 100%,0 100%);display:flex;align-items:center;
  gap:20px;padding-left:80px;color:var(--white);font-size:15px}
.topbar .item{display:flex;align-items:center;gap:8px}
.topbar .social{font-size:13px;font-weight:600}
.nav{position:absolute;top:104px;left:450px;display:flex;gap:42px;color:var(--white);
  font-size:15px;font-weight:500;letter-spacing:.5px}
.hero-title{position:absolute;left:168px;top:250px;color:var(--blue);font-size:43px;
  font-weight:700;line-height:52px}
.hero-text{position:absolute;left:168px;top:376px;width:450px;color:var(--white);font-size:15px;line-height:21px}
.hero-art{position:absolute;left:655px;top:170px;width:470px;height:400px;border-radius:48% 52% 40% 50%;
  background:radial-gradient(circle at 55% 45%,#dfe8ff 0%,#a9c2f5 55%,rgba(90,130,220,0) 75%)}
.start-title{position:absolute;top:788px;width:1200px;text-align:center;color:var(--white);
  font-size:37px;font-weight:500;letter-spacing:1px}
.start-text{position:absolute;top:846px;left:300px;width:600px;text-align:center;color:var(--white);
  font-size:16px;line-height:28px}

/* why */
.why{position:absolute;left:0;top:1011px;width:1200px;height:784px;background:var(--grey-bg)}
.why h2{position:absolute;top:70px;width:1200px;text-align:center;font-size:36px;font-weight:600}
.why-item{position:absolute;width:240px;font-size:14px;line-height:22px;color:var(--text-soft)}
.why-item h3{color:var(--blue);font-size:24px;font-weight:700;margin-bottom:4px}
.why-item.center{text-align:center}
.why-core{position:absolute;left:440px;top:290px;width:320px;height:320px;border-radius:50%;
  background:radial-gradient(circle,var(--blue-light) 0%,var(--blue) 55%,rgba(20,121,242,0) 72%)}
.num{position:absolute;width:62px;height:62px;border-radius:50%;
  background:radial-gradient(circle at 40% 35%,#fbd965,var(--gold-deep));
  display:flex;align-items:center;justify-content:center;font-size:30px;color:#222}

/* services */
.services{position:absolute;left:0;top:1795px;width:1200px;height:1010px;
  background:linear-gradient(120deg,#201d19 0%,#2d2820 45%,#3d321f 100%)}
.services h2{position:absolute;top:100px;width:1200px;text-align:center;color:var(--white);
  font-size:38px;font-weight:600;line-height:50px;letter-spacing:.5px}
.card{position:absolute;width:248px;height:284px;border:1px solid rgba(200,180,140,.45);
  text-align:center;color:var(--white)}
.card svg{position:absolute;left:74px;top:26px}
.card h3{position:absolute;top:158px;width:100%;color:var(--blue);font-size:21px;font-weight:500}
.card p{position:absolute;top:196px;left:20px;width:208px;font-size:13px;line-height:21px}

/* traffic */
.traffic{position:absolute;left:0;top:2805px;width:1200px;height:630px;background:var(--white)}
.traffic h2{position:absolute;left:155px;top:180px;font-size:37px;font-weight:600;line-height:50px}
.traffic p{position:absolute;left:160px;top:302px;width:380px;font-size:16px;line-height:27px;color:var(--text-soft)}
.dash{position:absolute;left:565px;top:165px;width:585px;height:355px;
  background:linear-gradient(135deg,#f7f8fc 0%,#e9edf8 60%,#c9dcfb 100%);border-radius:6px}

/* contact */
.contact{position:absolute;left:0;top:3435px;width:1200px;height:500px;
  background:linear-gradient(90deg,#1786f5 0%,#0f74ea 60%,#1d6ed6 100%)}
.contact-art{position:absolute;left:170px;top:100px;width:430px;height:300px;border-radius:12px;
  background:radial-gradient(circle at 45% 50%,#6fc0ff 0%,#3f9af8 45%,rgba(20,121,242,0) 75%)}
.contact h2{position:absolute;left:665px;top:118px;color:var(--white);font-size:30px;font-weight:600;letter-spacing:1px}
.field{position:absolute;height:37px;border:1px solid var(--white);color:var(--white);
  font-size:12px;padding:11px 10px}

/* quality */
.quality{position:absolute;left:0;top:3935px;width:1200px;height:610px;background:var(--white)}
.quality h2{position:absolute;left:168px;top:118px;color:var(--blue);font-size:41px;font-weight:600;
  line-height:50px;letter-spacing:.5px;text-transform:uppercase}
.quality p{position:absolute;left:175px;top:400px;width:420px;font-size:16px;line-height:27px;color:var(--text-soft)}
.quality-art{position:absolute;left:580px;top:55px;width:570px;height:580px;
  background:radial-gradient(ellipse at 50% 50%,#cdd3db 0%,#e6e9ee 45%,rgba(255,255,255,0) 72%)}

/* closing */
.closing{position:absolute;left:0;top:4530px;width:1200px;height:651px}
.closing .eyebrow{position:absolute;top:262px;width:1200px;text-align:center;color:var(--gold);
  font-size:11px;font-weight:600;letter-spacing:1px}
.closing h2{position:absolute;top:295px;width:1200px;text-align:center;color:var(--white);
  font-size:32px;font-weight:500;line-height:40px}
.copyright{position:absolute;top:593px;width:1200px;text-align:center;color:var(--white);font-size:11px}
.footer-social{position:absolute;right:170px;top:585px;display:flex;gap:26px;color:var(--white);
  font-size:16px;font-weight:700}
</style>
</head>
<body>

<section class="hero">
  <div class="topbar">
    <span class="item">
      <svg width="20" height="20" viewBox="0 0 24 24" fill="none" stroke="#fff" stroke-width="2"><path d="M5 3h4l2 5-3 2a12 12 0 0 0 6 6l2-3 5 2v4a2 2 0 0 1-2 2A17 17 0 0 1 3 5a2 2 0 0 1 2-2z"/></svg>
      +1 555 010 2040
    </span>
    <span class="item">
      <svg width="26" height="18" viewBox="0 0 26 18" fill="none" stroke="#fff" stroke-width="2"><rect x="1" y="1" width="24" height="16"/><path d="M1 1l12 9 12-9"/></svg>
      hello@brightvalecrew.example
    </span>
    <span class="social">Fb</span><span class="social">Tw</span><span class="social">Ig</span>
  </div>

  <div class="brand" style="left:140px;top:82px"><span class="dot"></span>Brightvale<br>Crew</div>

  <nav class="nav"><span>HOME</span><span>MORTAGES</span><span>WHY US</span><span>ABOUT US</span><span>CONTACT US</span></nav>

  <h1 class="hero-title">Full Service<br>Mortgage Marketing</h1>
  <p class="hero-text">Lorem ipsum dolor sit amet, consectetur adipiscing elit, sed do eiusmod tempor incididunt</p>
  <div class="btn" style="left:172px;top:456px;width:282px;height:40px;font-size:14px">Schedule Consultation</div>

  <div class="hero-art" role="img" aria-label="Illustration of a person with balloons beside a house shaped like a piggy bank with a gold coin"></div>

  <svg class="abs" style="left:0;top:660px" width="1200" height="351" viewBox="0 0 1200 351">
    <path d="M0 220 C300 60 650 10 960 40 C1070 52 1150 90 1200 130 L1200 351 L0 351 Z" fill="#4f9cf7"/>
    <path d="M0 232 C300 80 650 35 960 62 C1070 74 1150 110 1200 150 L1200 351 L0 351 Z" fill="#2a86f4"/>
    <path d="M0 245 C300 100 650 60 960 88 C1070 100 1150 135 1200 170 L1200 351 L0 351 Z" fill="var(--blue)"/>
  </svg>
  <h2 class="start-title">LET'S GET STARTED</h2>
  <p class="start-text">Lorem ipsum dolor sit amet, consectetur adipiscing elit, sed do eiusmod tempor &nbsp;exercitation ullamco commodo consequat.</p>
  <div class="btn" style="left:516px;top:918px;width:168px;height:44px;font-size:15px">Contact Us</div>
</section>

<section class="why">
  <h2>Why Choose Brightvale Crew?</h2>
  <div class="why-item center" style="left:480px;top:162px">
    <h3>Lorem ipsum</h3>Lorem ipsum dolor sit amet, consectetur adipiscing elit, dolore magna aliqua.
  </div>
  <div class="why-item" style="left:182px;top:405px">
    <h3>Lorem ipsum</h3>Lorem ipsum dolor sit amet, consectetur adipiscing elit, dolore magna aliqua.
  </div>
  <div class="why-item" style="left:812px;top:405px">
    <h3>Lorem ipsum</h3>Lorem ipsum dolor sit amet, consectetur adipiscing elit, dolore magna aliqua.
  </div>
  <div class="why-item center" style="left:480px;top:622px">
    <h3>Lorem ipsum</h3>Lorem ipsum dolor sit amet, consectetur adipiscing elit, dolore magna aliqua.
  </div>
  <div class="why-core" role="img" aria-label="Large blue decorative graphic at the centre of the four benefits"></div>
  <div class="num" style="left:566px;top:285px">1</div>
  <div class="num" style="left:698px;top:417px">2</div>
  <div class="num" style="left:568px;top:548px">3</div>
  <div class="num" style="left:437px;top:419px">4</div>
</section>

<section class="services">
  <h2>Whatever Your Company Needs.<br>We've Got You Covered</h2>

  <div class="card" style="left:205px;top:257px">
    <svg width="100" height="110" viewBox="0 0 100 110"><path d="M50 8 L90 45 H78 V80 H22 V45 H10 Z" fill="var(--gold)"/><text x="50" y="68" text-anchor="middle" font-size="30" font-weight="700" fill="#2b2620" font-family="Montserrat,sans-serif">$</text><path d="M8 100 Q40 82 70 92 L92 86" stroke="var(--gold-deep)" stroke-width="8" fill="none"/></svg>
    <h3>Service Name</h3><p>Lorem ipsum dolor sit amet, , dolore magna aliqua.</p>
  </div>
  <div class="card" style="left:475px;top:257px">
    <svg width="100" height="110" viewBox="0 0 100 110"><path d="M50 6 L88 20 V52 C88 78 70 94 50 104 C30 94 12 78 12 52 V20 Z" fill="var(--gold)"/><circle cx="50" cy="54" r="22" fill="none" stroke="#2b2620" stroke-width="5"/><path d="M40 54 l7 7 l13 -14" fill="none" stroke="#2b2620" stroke-width="5"/></svg>
    <h3>Service Name</h3><p>Lorem ipsum dolor sit amet, , dolore magna aliqua.</p>
  </div>
  <div class="card" style="left:745px;top:257px">
    <svg width="100" height="110" viewBox="0 0 100 110"><circle cx="62" cy="30" r="24" fill="var(--gold)"/><text x="62" y="40" text-anchor="middle" font-size="28" font-weight="700" fill="#2b2620" font-family="Montserrat,sans-serif">$</text><rect x="6" y="70" width="14" height="26" rx="3" fill="var(--gold)"/><path d="M24 92 H64 L94 74 L86 68 L62 80 H44" stroke="var(--gold)" stroke-width="8" fill="none"/></svg>
    <h3>Service Name</h3><p>Lorem ipsum dolor sit amet, , dolore magna aliqua.</p>
  </div>

  <div class="card" style="left:205px;top:562px">
    <svg width="100" height="110" viewBox="0 0 100 110"><path d="M50 36 L84 66 H74 V100 H26 V66 H16 Z" fill="var(--gold)"/><rect x="42" y="76" width="16" height="24" fill="#2b2620"/><circle cx="20" cy="22" r="9" fill="var(--gold)"/><circle cx="50" cy="14" r="9" fill="var(--gold)"/><circle cx="80" cy="22" r="9" fill="var(--gold)"/></svg>
    <h3 style="top:130px">Service Name</h3><p>Lorem ipsum dolor sit amet, , dolore magna aliqua.</p>
  </div>
  <div class="card" style="left:475px;top:562px">
    <svg width="100" height="110" viewBox="0 0 100 110"><path d="M34 70 L24 104 L38 96 L46 108 L50 80 Z M66 70 L76 104 L62 96 L54 108 L50 80 Z" fill="var(--gold-deep)"/><circle cx="50" cy="44" r="38" fill="var(--gold)"/><path d="M50 22 L72 42 H66 V64 H34 V42 H28 Z" fill="#2b2620"/><rect x="45" y="50" width="10" height="14" fill="var(--gold)"/></svg>
    <h3>Service Name</h3><p>Lorem ipsum dolor sit amet, , dolore magna aliqua.</p>
  </div>
  <div class="card" style="left:745px;top:562px">
    <svg width="100" height="120" viewBox="0 0 100 120"><path d="M50 4 L92 20 V56 C92 86 72 104 50 116 C28 104 8 86 8 56 V20 Z" fill="var(--gold)"/><path d="M50 16 L80 28 V56 C80 78 66 92 50 101 C34 92 20 78 20 56 V28 Z" fill="none" stroke="#2b2620" stroke-width="3"/><rect x="36" y="54" width="28" height="24" rx="3" fill="#2b2620"/><path d="M41 54 V46 a9 9 0 0 1 18 0 V54" fill="none" stroke="#2b2620" stroke-width="4"/></svg>
    <h3>Service Name</h3><p>Lorem ipsum dolor sit amet, , dolore magna aliqua.</p>
  </div>
</section>

<section class="traffic">
  <h2>Get More Traffic.<br>Get More Loans!</h2>
  <p>Lorem ipsum dolor sit amet, consectetur adipiscing elit, sed do eiusmod tempor incididunt ut labore et dolore magna aliqua. x ea commodo consequat.</p>
  <div class="btn" style="left:160px;top:470px;width:276px;height:44px;font-size:16px">Schedule a Call</div>
  <div class="dash" role="img" aria-label="Laptop and phone showing a website analytics dashboard with traffic charts"></div>
</section>

<section class="contact">
  <div class="contact-art" role="img" aria-label="Illustration of a support agent with headset at a laptop, with chat bubbles and a plant"></div>
  <h2>CONTACT US</h2>
  <div class="field" style="left:665px;top:193px;width:170px">First Name</div>
  <div class="field" style="left:858px;top:193px;width:170px">Second Name</div>
  <div class="field" style="left:665px;top:248px;width:170px">Email Address</div>
  <div class="field" style="left:858px;top:248px;width:170px">Telephone</div>
  <div class="field" style="left:665px;top:301px;width:363px;height:66px">Message</div>
  <div class="btn" style="left:662px;top:385px;width:114px;height:36px;font-size:14px;font-weight:500;letter-spacing:0">Submit</div>
</section>

<section class="quality">
  <div class="quality-art" role="img" aria-label="Photo of hands holding a small model house framed by a decorative shape"></div>
  <h2>Brightvale Crew<br>provide a<br>quick &amp; quality<br>services</h2>
  <p>Lorem ipsum dolor sit amet, consectetur adipiscing elit, sed do eiusmod tempor incididunt ut labore et dolore magna aliqua. x ea commodo consequat.</p>
  <div class="btn" style="left:174px;top:537px;width:275px;height:44px;font-size:16px">Book an Appointment</div>
</section>

<section class="closing">
  <svg class="abs" style="left:0;top:0" width="1200" height="651" viewBox="0 0 1200 651">
    <defs><linearGradient id="closingBg" x1="0" y1="0" x2="1" y2="1"><stop offset="0" stop-color="var(--dark)"/><stop offset="1" stop-color="var(--dark-warm)"/></linearGradient></defs>
    <path d="M0 0 C380 160 880 190 1200 110 L1200 651 L0 651 Z" fill="url(#closingBg)"/>
    <path d="M0 0 C380 160 880 190 1200 110" fill="none" stroke="#ffffff" stroke-opacity=".25" stroke-width="2"/>
  </svg>
  <div class="eyebrow">LET'S GET STARTED</div>
  <h2>Ready To Make a Real Change for<br>Your Mortgage Brokerage? Let's<br>Build this Thing Together!</h2>
  <div class="btn" style="left:416px;top:461px;width:220px;height:34px;font-size:11px">Setup a Free Meeting</div>
  <div class="brand" style="left:160px;top:548px;font-size:20px"><span class="dot" style="width:26px;height:26px"></span>Brightvale<br>Crew</div>
  <div class="copyright">© Copyright 2022. All Rights Reserved</div>
  <div class="footer-social"><span>Fb</span><span>Tw</span><span>G+</span><span>Rss</span></div>
</section>

</body>
</html>
```